Website for a web design agency

We are a website and marketing agency. We do website design, development, and well as Brindle and Quorvia advertising and analytics. We ourselves need a new website for our own brand. We are working on some designs in-house with our own designers, but we also wanted to see what outside designers would come up with.
We are starting off with the homepage, and here is the breakdown of the sections:
https://files.brindlework.example/sheet/d/7kqTr2VnPLwXeHsaMcY4oBfJzuGNtKdWiEh3Rx9pLmQb/view?mode=share
This doc also has many links to sites we have done, which you can take screenshots of for the portfolio section.
In terms of the "look" I am going for, I want to look high-end and very beautiful designs. I found this website that I like a lot that you can use some of the elements of, just as a starting point:
http://velmarkstudio.example/layouts/pixelbarn/html/ostrevo/index.html and here is another design option they have http://velmarkstudio.example/layouts/pixelbarn/html/ostrevo/index-4.html
I'm also uploading my logo. The logo matches the gold and black look from these websites, but I would be open to switching to another color scheme if needed.
This is the link to my very old website, which you can use for some of the dummy text, and a pic of myself. I will be taking more pics of myself:
https://theplumtreeandwillowgroup.example/
We need a homepage and a portfolio page right now, but if you are the winner, we will be hiring you to make additional pages.
Updates
More designs continue to come in even today, and I want to make sure no other designers are still submitting designs.
Target Market(s)
medium and large businesses owners, and non-profits
Number of Pages Required
1 page

```html
<!DOCTYPE html>
<html lang="en">
<head>
<meta charset="utf-8">
<title>Sorvane Strategies — Website Development & Digital Marketing</title>
<link href="https://fonts.googleapis.com/css2?family=Raleway:ital,wght@0,400;0,500;0,600;0,700;1,500;1,600&family=Montserrat:wght@600;700&display=swap" rel="stylesheet">
<style>
:root{
  --gold:#f0b323;
  --ink:#ffffff;
  --muted:#d8d8d2;
  --night:#000000;
  --charcoal:#232322;
  --olive:#363632;
  --panel:#3b3b37;
  --field:#ffffff;
  --blue:#2f7de1;
}
*{box-sizing:border-box;margin:0;padding:0}
html,body{width:1200px;height:3125px;overflow:hidden}
body{position:relative;background:var(--olive);color:var(--ink);font-family:"Raleway",sans-serif}
.abs{position:absolute}
a{color:inherit;text-decoration:none}

/* header */
.site-header{left:0;top:0;width:1200px;height:56px;background:var(--night)}
.brand{left:226px;top:13px;line-height:1}
.brand-name{font-family:"Montserrat",sans-serif;font-weight:700;font-size:21px;color:var(--gold);letter-spacing:1px}
.brand-tag{display:block;font-size:8px;letter-spacing:4.2px;color:var(--gold);margin-top:2px;font-weight:600}
.main-nav{left:600px;top:21px;display:flex;gap:0;font-size:11px}
.main-nav a{margin-right:34px}

/* bands */
.band-hero{left:0;top:56px;width:1200px;height:457px;background:var(--charcoal)}
.band-quote{left:0;top:1082px;width:1200px;height:227px;background:var(--charcoal)}

.btn{display:flex;align-items:center;justify-content:center;background:var(--gold);color:var(--ink);font-weight:700;font-size:11px;border-radius:2px}

.hero-title{left:226px;top:118px;font-family:"Montserrat",sans-serif;font-weight:600;font-size:36px}
.hero-sub{left:226px;top:172px;font-size:15.5px;line-height:21px;width:300px}
.hero-btn{left:226px;top:232px;width:124px;height:34px}

.video{left:571px;top:99px;width:349px;height:199px;box-shadow:0 4px 14px rgba(0,0,0,.5)}
.video-still{left:0;top:0;width:349px;height:170px;background:linear-gradient(120deg,#7c7c78,#a9a8a3 55%,#6d645e)}
.video-caption{left:8px;top:118px;font-family:"Montserrat",sans-serif;font-weight:600;font-size:17px;line-height:19px;color:#fff;text-shadow:0 1px 3px #000}
.video-caption span{display:block;padding-left:29px;font-size:16px}
.video-play{left:150px;top:66px}
.video-bar{left:0;top:170px;width:349px;height:29px;background:#161616}
.video-progress{left:0;top:170px;width:114px;height:3px;background:var(--gold)}
.video-time{right:60px;top:180px;font-size:8px;color:#ddd}

/* services */
.services{left:226px;top:338px;width:749px;height:282px;background:var(--panel);box-shadow:0 6px 14px rgba(0,0,0,.35)}
.service{width:160px;text-align:center;color:var(--gold);font-size:11.5px}
.service svg{display:block;margin:0 auto 6px}
.service .arrow{display:block;margin:10px auto 0}

/* portfolio */
.monitor-screen{left:226px;top:718px;width:353px;height:208px;background:#111;border-radius:6px;padding:10px}
.monitor-shot{width:100%;height:100%;background:linear-gradient(135deg,#0d2a5a,#1e4f8f 55%,#8aa5c9);border-top:22px solid #fff;border-bottom:16px solid #fff}
.monitor-stand{left:355px;top:926px;width:97px;height:63px;background:linear-gradient(90deg,#9a9a9a,#e2e2e2,#8c8c8c);clip-path:polygon(20% 0,80% 0,100% 85%,100% 100%,0 100%,0 85%)}
.dots{display:flex;gap:4px}
.dots i{width:5px;height:5px;border-radius:50%;background:#fff;display:block}
.dots i.on{background:#e3232b}
.portfolio-dots{left:386px;top:1030px}
.section-title{font-weight:600;font-size:24px}
.portfolio-title{left:622px;top:704px}
.portfolio-lead{left:622px;top:742px;width:350px;font-style:italic;font-weight:500;font-size:16px;line-height:22px}
.portfolio-copy{left:623px;top:803px;width:345px;font-size:11.5px;line-height:17px;color:var(--muted)}
.portfolio-btn{left:623px;top:949px;width:113px;height:29px}
.client-photo{left:795px;top:928px;width:170px;height:378px;background:linear-gradient(180deg,#3a2a22 0%,#c9a088 18%,#f1f1ef 40%,#e6e6e4 70%,#5a5a5a 100%);border-radius:60px 60px 0 0}

/* testimonial */
.quote-mark{left:236px;top:1120px;font-family:"Montserrat",sans-serif;font-size:34px;font-style:italic;color:var(--gold)}
.quote-title{left:268px;top:1131px;font-weight:600;font-size:17.5px}
.quote-body{left:268px;top:1157px;width:480px;font-style:italic;font-weight:600;font-size:11.2px;line-height:22.5px}
.quote-dots{left:590px;top:1250px}

/* together */
.together-title{left:224px;top:1431px;width:320px;line-height:31px}
.together-copy{left:224px;top:1503px;width:320px;font-size:14.5px;line-height:21px}
.together-btn{left:224px;top:1577px;width:112px;height:29px}
.search-photo{left:600px;top:1367px;width:600px;height:312px;background:linear-gradient(115deg,#f4f4f4 0%,#e6e7ea 30%,#1a1a1a 33%,#2a2a2a 36%,#eef2f9 40%,#dfe8f5 100%)}

/* help box */
.help{left:226px;top:1736px;width:749px;height:929px;background:var(--charcoal)}
.help-title{left:54px;top:50px}
.help-intro{left:57px;top:82px;width:320px;font-size:11.5px;line-height:17px;font-weight:500}
.help-lead{left:57px;top:148px;font-size:11.5px;font-weight:500}
.pillar{width:190px}
.pillar h3{color:var(--gold);font-weight:600;font-size:15px;margin:8px 0 8px}
.pillar p{font-size:11px;line-height:17px;font-weight:500}
.pillar a{display:block;margin-top:8px;color:var(--gold);font-weight:700;font-size:10px;text-decoration:underline}
.gain-title{left:56px;top:400px}
.gain-copy{left:56px;top:436px;width:400px;font-size:14px;line-height:19px}
.value{width:130px}
.value h4{color:var(--gold);font-weight:700;font-size:10px;margin:9px 0 4px}
.value p{font-size:9.2px;line-height:12px}
.team-photo{left:54px;top:656px;width:205px;height:216px;background:linear-gradient(180deg,#f4f4f4 0%,#d7b49f 40%,#f0d6c8 75%,#e9e2dc 100%)}
.team-title{left:283px;top:656px}
.team-copy{left:283px;top:696px;width:420px;font-size:11px;line-height:14px}
.avatar{border-radius:50%}
.team-next{left:690px;top:813px}

/* footer */
.site-footer{left:0;top:2723px;width:1200px;height:346px;background:var(--charcoal)}
.foot-head{font-size:10px;font-weight:700;letter-spacing:.3px;padding-bottom:4px;border-bottom:2px solid var(--gold);display:inline-block}
.foot-text{font-size:10.2px;line-height:15px}
.foot-list{list-style:none;font-size:10.5px}
.foot-list li{margin-bottom:15px}
.news-input{width:225px;height:25px;background:#000;font-size:7px;padding:9px 11px;color:#ddd}
.form-label{font-size:11px}
.form-field{background:var(--field);color:#bbb;font-size:9px;padding:10px 9px}
.contact-row{display:flex;align-items:center;gap:8px;font-size:9px;font-weight:700}
.site-bottom{left:0;top:3069px;width:1200px;height:56px;background:var(--night);font-size:8.5px;font-weight:600}
.social{display:flex;gap:14px}
.social span{width:21px;height:21px;border-radius:50%;background:#fff;display:block}
</style>
</head>
<body>

<header class="site-header abs">
  <div class="brand abs"><span class="brand-name">SORVANE</span><span class="brand-tag">STRATEGIES</span></div>
  <nav class="main-nav abs"><a>Home</a><a>About</a><a>Service</a><a>Portfolio</a><a>Team</a><a>Contact</a></nav>
</header>

<section class="band-hero abs"></section>
<h1 class="hero-title abs">We build Value</h1>
<p class="hero-sub abs">Enterprise Level Website Development and Online Digital Marketing.</p>
<a class="hero-btn btn abs">Get a Quote</a>

<div class="video abs">
  <div class="video-still abs" role="img" aria-label="Video still of the founder speaking to camera"></div>
  <svg class="video-play abs" width="44" height="44" viewBox="0 0 44 44"><circle cx="22" cy="22" r="21" fill="rgba(255,255,255,.25)"/><path d="M16 11 L33 22 L16 33Z" fill="#fff"/></svg>
  <div class="video-caption abs">Marcus Delvane<span>web developer</span></div>
  <div class="video-bar abs"></div>
  <div class="video-progress abs"></div>
  <svg class="abs" style="left:12px;top:178px" width="120" height="12" viewBox="0 0 120 12" fill="#fff">
    <path d="M2 2 L9 6 L2 10Z"/><rect x="26" y="2" width="2" height="8"/><rect x="31" y="2" width="2" height="8"/>
    <rect x="50" y="2" width="8" height="8"/><path d="M76 2 L82 6 L76 10Z"/><rect x="83" y="2" width="1.5" height="8"/>
    <path d="M108 4 h3 l4 -3 v10 l-4 -3 h-3Z"/>
  </svg>
  <div class="video-time abs">03:47 / 10:00</div>
  <svg class="abs" style="right:40px;top:179px" width="11" height="11" viewBox="0 0 12 12"><circle cx="6" cy="6" r="3.5" fill="none" stroke="#fff" stroke-width="2.5" stroke-dasharray="2 1.4"/></svg>
  <svg class="abs" style="right:10px;top:180px" width="14" height="10" viewBox="0 0 14 10"><rect x="1" y="1" width="12" height="8" fill="none" stroke="#fff" stroke-width="1.4"/></svg>
</div>

<section class="services abs">
  <div class="service abs" style="left:25px;top:45px">
    <svg width="32" height="32" viewBox="0 0 32 32" fill="none" stroke="var(--gold)" stroke-width="1.4"><rect x="3" y="4" width="24" height="20"/><path d="M3 9h24M12 13l-3 3 3 3M18 13l3 3-3 3M16 12l-2 8"/><circle cx="26" cy="25" r="4"/></svg>
    Web Design<svg class="arrow" width="24" height="10" viewBox="0 0 24 10" fill="none" stroke="var(--gold)" stroke-width="1.4"><path d="M1 5h21M17 1l5 4-5 4"/></svg>
  </div>
  <div class="service abs" style="left:285px;top:45px">
    <svg width="32" height="32" viewBox="0 0 32 32" fill="none" stroke="var(--gold)" stroke-width="1.4"><rect x="7" y="2" width="18" height="28"/><path d="M10 7h12M10 11h12M10 15h6M10 19h12M10 23h12M10 27h8"/></svg>
    Landing Pages<svg class="arrow" width="24" height="10" viewBox="0 0 24 10" fill="none" stroke="var(--gold)" stroke-width="1.4"><path d="M1 5h21M17 1l5 4-5 4"/></svg>
  </div>
  <div class="service abs" style="left:541px;top:45px">
    <svg width="34" height="32" viewBox="0 0 34 32" fill="none" stroke="var(--gold)" stroke-width="1.4"><rect x="4" y="20" width="5" height="10"/><rect x="12" y="16" width="5" height="14"/><rect x="20" y="18" width="5" height="12"/><rect x="28" y="12" width="5" height="18"/><path d="M6 12l8-6 8 5 9-8"/><circle cx="6" cy="12" r="2"/><circle cx="14" cy="6" r="2"/><circle cx="22" cy="11" r="2"/></svg>
    Analytics &amp; optimisation<svg class="arrow" width="24" height="10" viewBox="0 0 24 10" fill="none" stroke="var(--gold)" stroke-width="1.4"><path d="M1 5h21M17 1l5 4-5 4"/></svg>
  </div>
  <div class="service abs" style="left:25px;top:157px">
    <svg width="32" height="32" viewBox="0 0 32 32" fill="none" stroke="var(--gold)" stroke-width="1.4"><rect x="3" y="6" width="22" height="18"/><path d="M3 10h22"/><circle cx="26" cy="6" r="4"/><path d="M12 14v8l2-2 2 4 2-1-2-4h3Z"/></svg>
    PPC &amp; Funnels<svg class="arrow" width="24" height="10" viewBox="0 0 24 10" fill="none" stroke="var(--gold)" stroke-width="1.4"><path d="M1 5h21M17 1l5 4-5 4"/></svg>
  </div>
  <div class="service abs" style="left:285px;top:157px">
    <svg width="32" height="32" viewBox="0 0 32 32" fill="none" stroke="var(--gold)" stroke-width="1.4"><rect x="2" y="3" width="28" height="26"/><path d="M2 8h28"/><circle cx="16" cy="16" r="5"/><rect x="6" y="23" width="20" height="4" fill="var(--gold)"/></svg>
    Donation Pages<svg class="arrow" width="24" height="10" viewBox="0 0 24 10" fill="none" stroke="var(--gold)" stroke-width="1.4"><path d="M1 5h21M17 1l5 4-5 4"/></svg>
  </div>
  <div class="service abs" style="left:541px;top:157px">
    <svg width="32" height="32" viewBox="0 0 32 32" fill="none" stroke="var(--gold)" stroke-width="1.4"><rect x="4" y="7" width="24" height="20"/><rect x="10" y="2" width="10" height="6"/><path d="M14 13l6 4-6 4Z"/><path d="M8 30h16"/></svg>
    Video Marketing<svg class="arrow" width="24" height="10" viewBox="0 0 24 10" fill="none" stroke="var(--gold)" stroke-width="1.4"><path d="M1 5h21M17 1l5 4-5 4"/></svg>
  </div>
</section>

<div class="monitor-screen abs"><div class="monitor-shot" role="img" aria-label="Screenshot of a client website for Halvard Productions"></div></div>
<div class="monitor-stand abs"></div>
<div class="portfolio-dots dots abs"><i></i><i></i><i></i><i class="on"></i></div>

<h2 class="portfolio-title section-title abs">Our Portfolio</h2>
<p class="portfolio-lead abs">These are some of my favorite projects we've done for our clients</p>
<p class="portfolio-copy abs">Lorem ipsum dolor sit amet, consectetur adipiscing elit, sed do eiusmod tempor incididunt ut labore et dolore magna aliqua. Quis ipsum suspendisse ultrices gravida. Risus commodo viverra maecenas accumsan lacus vel facilisis. Lorem ipsum dolor sit amet, consectetur adipiscing elit, sed do eiusmod tempor incididunt ut labore et dolore magna aliqua. Quis ipsum suspendisse ultrices gravida. Risus commodo viverra maecenas.</p>
<a class="portfolio-btn btn abs">View Gallery</a>

<section class="band-quote abs"></section>
<div class="client-photo abs" role="img" aria-label="Photo of a smiling client holding a phone"></div>
<div class="quote-mark abs">“</div>
<h3 class="quote-title abs">Incredible value and peace of mind</h3>
<p class="quote-body abs">Sorvane strategies Services provide us with insight into the health of our network something we couldn't quantify in the past. The remote monitoring capabilities help us identify small issues before they become major problems and save time and money by anticipating server upgrades.</p>
<div class="quote-dots dots abs"><i class="on"></i><i></i><i></i></div>

<h2 class="together-title section-title abs">Let's build your business online, together.</h2>
<p class="together-copy abs">I want to build your site or get you higher on Brindle. Unlike big agencies, I want to hold your hand throughout the process.</p>
<a class="together-btn btn abs">Case Study</a>
<div class="search-photo abs" role="img" aria-label="Close-up photo of a phone showing a search results page"></div>

<section class="help abs">
  <h2 class="help-title section-title abs">How We Help ?</h2>
  <p class="help-intro abs">Whether you are just starting out or already a successful business, having a successful online presence is always a central part of your business.</p>
  <p class="help-lead abs">Here is how we can help you :</p>

  <div class="pillar abs" style="left:57px;top:188px">
    <svg width="34" height="32" viewBox="0 0 34 32" fill="none" stroke="var(--gold)" stroke-width="1.4"><rect x="2" y="2" width="12" height="10"/><rect x="20" y="2" width="12" height="10"/><rect x="10" y="16" width="14" height="10"/><path d="M2 30h30M8 12v4M26 12v4"/></svg>
    <h3>Create</h3><p>I can help you figure out what makes you unique. It's your unique selling point that helps you stand out from the other millions.</p><a>Read More</a>
  </div>
  <div class="pillar abs" style="left:279px;top:188px">
    <svg width="42" height="32" viewBox="0 0 42 32" fill="none" stroke="var(--gold)" stroke-width="1.4"><rect x="1" y="1" width="40" height="30"/><path d="M1 6h40M5 11h10M5 16h10M5 21h10M5 26h10M19 11h18M19 16h18M19 21h14M19 26h18"/></svg>
    <h3>Build</h3><p>Your website is your own special place online for what you are trying to bring to the world. I help make it stand out for.</p><a>Read More</a>
  </div>
  <div class="pillar abs" style="left:498px;top:188px">
    <svg width="20" height="32" viewBox="0 0 20 32" fill="none" stroke="var(--gold)" stroke-width="1.4"><path d="M10 1c5 5 6 12 4 20h-8C4 13 5 6 10 1Z"/><circle cx="10" cy="11" r="2.5"/><path d="M6 17l-4 6v4l4-4M14 17l4 6v4l-4-4M8 24v5M12 24v5"/></svg>
    <h3>Market</h3><p>Between SEO, SEM, social, blogging, &amp; email, web marketing can become overwhelming. I help you figure out the right path for growth.</p><a>Read More</a>
  </div>

  <h2 class="gain-title section-title abs">What you'll get</h2>
  <p class="gain-copy abs">I want to share our values with you so you can see what it's like working with me.</p>

  <div class="value abs" style="left:55px;top:484px">
    <svg width="32" height="32" viewBox="0 0 32 32" fill="none" stroke="var(--gold)" stroke-width="1.6"><circle cx="16" cy="16" r="14"/><circle cx="16" cy="9" r="2"/><path d="M9 13h14M16 13v7l-3 6M16 20l3 6"/></svg>
    <h4>Assessibility</h4><p>You get my actual cell phone number and are welcome to call me 24/7</p>
  </div>
  <div class="value abs" style="left:221px;top:484px">
    <svg width="34" height="32" viewBox="0 0 34 32" fill="none" stroke="var(--gold)" stroke-width="1.4"><rect x="14" y="2" width="16" height="14"/><circle cx="22" cy="9" r="3"/><path d="M2 22h8l6 3h8l6-4M2 30h10l12-3"/></svg>
    <h4>Affordability</h4><p>No small lettering or big corporations here. I promise to give you the best value..</p>
  </div>
  <div class="value abs" style="left:410px;top:484px">
    <svg width="32" height="32" viewBox="0 0 32 32" fill="none" stroke="var(--gold)" stroke-width="1.4"><path d="M16 7a7 7 0 0 0-4 12.7V23h8v-3.3A7 7 0 0 0 16 7Z"/><path d="M13 26h6M14 29h4M16 1v3M5 5l2 2M27 5l-2 2M2 15h3M27 15h3"/></svg>
    <h4>Creativity</h4><p>Struggling with what exactly you need? No problem! I'm here to be your brain.</p>
  </div>
  <div class="value abs" style="left:594px;top:484px">
    <svg width="32" height="30" viewBox="0 0 32 30" fill="none" stroke="var(--gold)" stroke-width="1.8"><path d="M16 28C6 20 2 15 2 9a7 7 0 0 1 14-2 7 7 0 0 1 14 2c0 6-4 11-14 19Z"/></svg>
    <h4>Care and Love</h4><p>Yes, I put my sweat tears and energy into my projects and my customers.</p>
  </div>

  <div class="team-photo abs" role="img" aria-label="Portrait photo of the founder"></div>
  <h2 class="team-title section-title abs">Our Team</h2>
  <p class="team-copy abs">Lorem ipsum dolor sit amet, consectetur adipiscing elit, usmod temporincididunt ut labore et ipsum suspendisse ultrices gravida.</p>
  <div class="avatar abs" style="left:291px;top:779px;width:92px;height:92px;background:radial-gradient(circle at 50% 40%,#8d7aa0,#4a3d70)" role="img" aria-label="Team member portrait"></div>
  <div class="avatar abs" style="left:408px;top:769px;width:112px;height:112px;background:radial-gradient(circle at 50% 40%,#7fb0f0,var(--blue));border:3px solid #2b5fb0;box-shadow:0 0 12px rgba(47,125,225,.6)" role="img" aria-label="Team member portrait"></div>
  <div class="avatar abs" style="left:556px;top:779px;width:92px;height:92px;background:radial-gradient(circle at 50% 40%,#6d7ab8,#2e3a7a)" role="img" aria-label="Team member portrait"></div>
  <svg class="team-next abs" width="12" height="22" viewBox="0 0 12 22" fill="none" stroke="var(--gold)" stroke-width="1.6"><path d="M1 1l10 10L1 21"/></svg>
</section>

<footer class="site-footer abs">
  <div class="abs" style="left:225px;top:38px;width:215px">
    <span class="foot-head">ABOUT US</span>
    <p class="foot-text" style="margin-top:10px">We are a website and marketing agency. We do website design, development, and well as Brindle and Quorvia advertising and analytics.</p>
    <span class="foot-head" style="margin-top:12px">NEWSLETTER</span>
    <p class="foot-text" style="margin-top:10px">Sign up for out monthly newsletter to stay current on all your compliance concerns.</p>
    <p style="font-size:9.5px;font-weight:700;margin-top:14px">EMAIL ADDRESS</p>
    <div class="news-input" style="margin-top:10px">JON.DOE@MAIL.COM</div>
    <a class="btn" style="width:81px;height:25px;margin-top:20px;font-size:7px">SUBMIT</a>
  </div>

  <div class="abs" style="left:518px;top:38px">
    <span class="foot-head">COMPANY</span>
    <ul class="foot-list" style="margin-top:12px"><li>Home</li><li>Services</li><li>Portfolio</li><li>Team</li></ul>
    <span class="foot-head" style="margin-top:12px">CONTACT</span>
    <div class="contact-row" style="margin-top:18px"><svg width="22" height="22" viewBox="0 0 22 22" fill="none" stroke="#fff" stroke-width="1.4"><circle cx="11" cy="11" r="10"/><rect x="6" y="7.5" width="10" height="7"/><path d="M6 8l5 4 5-4"/></svg>info@sorvane.example</div>
    <div class="contact-row" style="margin-top:14px"><svg width="22" height="22" viewBox="0 0 22 22" fill="none" stroke="#fff" stroke-width="1.4"><circle cx="11" cy="11" r="10"/><path d="M8 6l2 3-1 1.5c.7 1.5 1.8 2.6 3.3 3.3L14 13l3 2-1 2c-5 0-9-4-9-9Z"/></svg>555-014-2270</div>
  </div>

  <div class="abs" style="left:701px;top:38px;width:274px">
    <span class="foot-head">Get in Touch</span>
    <span class="form-label abs" style="left:2px;top:46px">Full name *</span>
    <span class="form-label abs" style="left:148px;top:46px">Email Address *</span>
    <div class="form-field abs" style="left:2px;top:67px;width:125px;height:30px">Full name</div>
    <div class="form-field abs" style="left:149px;top:67px;width:125px;height:30px">Email</div>
    <span class="form-label abs" style="left:3px;top:138px">Message *</span>
    <div class="form-field abs" style="left:3px;top:160px;width:271px;height:76px">Message</div>
    <a class="btn abs" style="left:3px;top:233px;width:271px;height:30px;font-size:9px">Submit</a>
  </div>
</footer>

<div class="site-bottom abs">
  <span class="abs" style="left:228px;top:23px">© 2021 Sorvane . All Rights Reserved</span>
  <div class="social abs" style="left:517px;top:17px" aria-label="Social profiles"><span></span><span></span><span></span><span></span><span></span></div>
  <span class="abs" style="left:827px;top:23px">Privacy Policy &amp; Terms of Service</span>
</div>

</body>
</html>
```